Current Employment Opportunities Email Template

We would like to redesign our internal job listing email template we send out each month. The email service we use is MailChimp and would like the template to be easy to edit when updating job postings. I attached an example below.

Font styles to use
Sans Serif

Colors

Designer to choose colors to be used in the design.

```html
<!DOCTYPE html>
<html lang="en">
<head>
<meta charset="utf-8">
<title>Current Opportunities – Bishop Works Inc.</title>
<link rel="stylesheet" href="https://fonts.googleapis.com/css2?family=Open+Sans:wght@300;400;600;700&family=Roboto+Condensed:wght@700&display=swap">
<style>
  :root {
    --page-bg: #f7f7f7;
    --card-bg: #ffffff;
    --ink: #1f1f1f;
    --body-text: #2e2e2e;
    --teal: #3f6e6c;
    --band: #ecf0ef;
    --border: #e1e4e3;
    --cta: #d93a0a;
    --link: #3f6e6c;
  }
  * { box-sizing: border-box; margin: 0; padding: 0; }
  html, body { width: 717px; height: 1200px; overflow: hidden; }
  body {
    background: var(--page-bg);
    font-family: "Open Sans", Arial, sans-serif;
    color: var(--body-text);
    position: relative;
  }
  .preheader {
    position: absolute; top: 22px; left: 0; width: 717px;
    text-align: center; font-size: 8px; line-height: 12px; color: var(--ink);
  }
  .preheader a { color: var(--link); text-decoration: none; }

  .email {
    position: absolute; left: 121px; top: 45px; width: 475px; height: 1099px;
    background: var(--card-bg);
    box-shadow: 0 14px 12px -12px rgba(0,0,0,0.25);
  }
  .brand {
    position: absolute; left: 0; width: 100%; height: 30px;
    font-family: "Open Sans", Arial, sans-serif;
    font-weight: 700; font-size: 22px; line-height: 30px; letter-spacing: 0.5px; color: var(--ink);
    display: flex; justify-content: center; align-items: center; gap: 7px;
  }
  .brand-mark { width: 10px; height: 10px; background: var(--ink); display: inline-block; }
  .brand--header { top: 24px; }
  .brand--footer { top: 1020px; }

  .hero {
    position: absolute; left: 0; top: 81px; width: 475px; height: 204px;
    overflow: hidden; text-align: center; color: #fff;
  }
  .hero-photo {
    position: absolute; inset: 0;
    background: linear-gradient(100deg, #5b7f7d 0%, #6f918f 40%, #7a9d9b 70%, #6d908e 100%);
  }
  .hero-photo::after {
    content: ""; position: absolute; left: 0; right: 0; bottom: 0; height: 90px;
    background: linear-gradient(to bottom, rgba(60,95,93,0), rgba(60,95,93,0.55));
  }
  .hero-title {
    position: absolute; top: 55px; left: 0; width: 100%;
    font-family: "Roboto Condensed", "Arial Narrow", sans-serif; font-weight: 700;
    font-size: 29px; line-height: 34px; letter-spacing: -0.2px;
  }
  .hero-rule {
    position: absolute; top: 104px; left: 51px; width: 373px; height: 1px;
    background: rgba(255,255,255,0.55);
  }
  .hero-subtitle {
    position: absolute; top: 115px; left: 50px; width: 375px;
    font-size: 15px; line-height: 20px; font-weight: 400;
  }

  .intro {
    position: absolute; top: 322px; left: 40px; width: 395px;
    text-align: center; font-size: 10.5px; line-height: 15.5px; color: var(--ink);
  }

  .openings {
    position: absolute; left: 0; top: 441px; width: 475px; height: 536px;
    background: var(--band);
    clip-path: polygon(0 16px, 100% 0, 100% 100%, 0 100%);
  }
  .openings-title {
    position: absolute; top: 56px; left: 0; width: 100%; text-align: center;
    font-family: "Roboto Condensed", "Arial Narrow", sans-serif; font-weight: 700;
    font-size: 24px; line-height: 28px; color: var(--teal);
  }
  .job-grid {
    position: absolute; top: 107px; left: 36px;
    display: grid; grid-template-columns: 191px 191px; grid-auto-rows: 186px;
    column-gap: 22px; row-gap: 20px;
  }
  .job-card {
    position: relative; height: 186px; background: var(--card-bg);
    border: 1px solid var(--border); text-align: center;
  }
  .job-card > * { position: absolute; left: 0; width: 100%; }
  .job-city {
    top: 24px;
    font-family: "Roboto Condensed", "Arial Narrow", sans-serif; font-weight: 700;
    font-size: 21px; line-height: 26px; color: var(--teal);
  }
  .job-role { top: 53px; font-size: 12px; font-weight: 300; color: var(--ink); line-height: 16px; }
  .job-location { top: 71px; font-size: 10px; color: var(--ink); line-height: 14px; }
  .job-summary {
    top: 88px; left: 15px; width: 159px;
    font-size: 9.6px; font-weight: 600; letter-spacing: 0.3px; line-height: 14px;
    color: var(--ink);
  }
  .job-button {
    top: 124px; left: 34px; width: 122px; height: 33px;
    background: var(--cta); color: #fff; text-decoration: none;
    font-size: 11px; font-weight: 700; line-height: 33px; border-radius: 1px;
  }
</style>
</head>
<body>
  <p class="preheader">Having trouble viewing this email? <a href="#">Open in a browser window</a></p>

  <main class="email">
    <div class="brand brand--header"><span class="brand-mark"></span>BISHOP WORKS INC.</div>

    <section class="hero">
      <div class="hero-photo" role="img" aria-label="Blurred city skyline photo with a teal tint"></div>
      <h1 class="hero-title">Today’s Talent Opportunities</h1>
      <div class="hero-rule"></div>
      <p class="hero-subtitle">Want to be a part of the most efficient and elite team in the industry?</p>
    </section>

    <p class="intro">We’ve got a list of opportunities here at Bishop Works that we’d love for you to strive for! These openings allow you to fully utilize your strengths, walk alongside us as we grow exponentially farther than we could ever dream, and leverage your successes to climb your way up the ladder of professional growth and leadership within our organization!</p>

    <section class="openings">
      <h2 class="openings-title">Current Opportunities</h2>
      <div class="job-grid">
        <article class="job-card">
          <h3 class="job-city">Dallas</h3>
          <p class="job-role">Lead Restoration Technician</p>
          <p class="job-location">Dallas, TX</p>
          <p class="job-summary">Restoration Technician in the Dallas/Ft. Worth Area</p>
          <a class="job-button" href="#">Learn More</a>
        </article>
        <article class="job-card">
          <h3 class="job-city">Dallas</h3>
          <p class="job-role">Lead Restoration Technician</p>
          <p class="job-location">Dallas, TX</p>
          <p class="job-summary">Restoration Technician in the Dallas/Ft. Worth Area</p>
          <a class="job-button" href="#">Learn More</a>
        </article>
        <article class="job-card">
          <h3 class="job-city">Dallas</h3>
          <p class="job-role">Lead Restoration Technician</p>
          <p class="job-location">Dallas, TX</p>
          <p class="job-summary">Restoration Technician in the Dallas/Ft. Worth Area</p>
          <a class="job-button" href="#">Learn More</a>
        </article>
        <article class="job-card">
          <h3 class="job-city">Dallas</h3>
          <p class="job-role">Lead Restoration Technician</p>
          <p class="job-location">Dallas, TX</p>
          <p class="job-summary">Restoration Technician in the Dallas/Ft. Worth Area</p>
          <a class="job-button" href="#">Learn More</a>
        </article>
      </div>
    </section>

    <div class="brand brand--footer"><span class="brand-mark"></span>BISHOP WORKS INC.</div>
  </main>
</body>
</html>
```